Carpentry and Building Business Card

I'm looking for a business card that is minimalistic and that incorporates the theme of my Velmor logo.
On one side I'd like the VELMOR logo with my details on the other side.
Double sided with curved edges

Target Market(s)

Construction / renovation
Adults

Industry/Entity Type

Tradesman

Contact Information for Business Card

Logo on one side, details on the other

Colors

Designer to choose only greyscale colors for use in the design.

Requirements
Must have
• Nilo Petrakis
VELMOR CONSTRUCT
Carpentry & Building Services
0481236574
Velmorconstruct@brixmail.com
Lic No. 718263D
Nice to have
• Fb and insta icons. @velmorconstruct
Should not have
• No hammer or tool icons please.

No address line.

```html
<!DOCTYPE html>
<html lang="en">
<head>
<meta charset="UTF-8">
<title>Velmor Construct – Business Card</title>
<link href="https://fonts.googleapis.com/css2?family=Playfair+Display:wght@700&family=Arimo:wght@400&display=swap" rel="stylesheet">
<style>
  :root {
    --bg: #e4e4e4;
    --card-dark: #141414;
    --card-light: #ffffff;
    --ink: #111111;
    --ink-soft: #5a5a5a;
    --name-light: #f2f2f2;
  }
  * { margin: 0; padding: 0; box-sizing: border-box; }
  html, body {
    width: 1200px; height: 900px; overflow: hidden;
    background: var(--bg);
  }
  .canvas {
    position: relative; width: 1200px; height: 900px;
    display: flex; flex-direction: column; align-items: center; justify-content: center;
    gap: 50px;
  }
  .card {
    width: 560px; height: 320px;
    border-radius: 28px;
    box-shadow: 0 10px 30px rgba(0,0,0,0.18);
    position: relative;
  }
  .card--front {
    background: var(--card-dark);
    display: flex; align-items: center; justify-content: center;
  }
  .card--back {
    background: var(--card-light);
    display: flex; flex-direction: column; align-items: center;
    padding-top: 30px;
  }
  .brand-name {
    font-family: "Arimo", sans-serif;
    font-weight: 400;
    letter-spacing: 0;
    line-height: 1;
  }
  .card--front .brand-name { color: var(--name-light); font-size: 48px; }
  .card--back .brand-name { color: var(--ink); font-size: 26px; }
  .holder {
    font-family: "Playfair Display", serif;
    font-weight: 700; font-size: 25px; color: var(--ink);
    margin-top: 14px;
  }
  .details {
    font-family: "Arimo", sans-serif;
    font-size: 13px; line-height: 1.35; color: var(--ink-soft);
    text-align: center; margin-top: 4px;
  }
  .social { display: flex; gap: 10px; margin-top: 8px; }
  .social__item { display: flex; flex-direction: column; align-items: center; }
  .social__square {
    width: 20px; height: 20px; border-radius: 4px; background: var(--ink);
  }
  .social__label {
    font-family: "Arimo", sans-serif; font-size: 6px; color: var(--ink-soft); margin-top: 2px;
  }
  .handle {
    font-family: "Arimo", sans-serif; font-size: 14px; color: var(--ink); margin-top: 3px;
  }
</style>
</head>
<body>
<main class="canvas">
  <section class="card card--front" aria-label="Card front">
    <span class="brand-name">Velmor</span>
  </section>

  <section class="card card--back" aria-label="Card back">
    <span class="brand-name">Velmor</span>
    <h1 class="holder">Nilo Petrakis</h1>
    <p class="details">
      VELMOR CONSTRUCT<br>
      Carpentry &amp; Building Services<br>
      0481236574<br>
      Velmorconstruct@brixmail.com<br>
      Lic No. 718263D
    </p>
    <div class="social">
      <div class="social__item"><span class="social__square"></span><span class="social__label">Friendlink</span></div>
      <div class="social__item"><span class="social__square"></span><span class="social__label">Snapframe</span></div>
    </div>
    <p class="handle">@velmorconstruct</p>
  </section>
</main>
</body>
</html>
```